KW Depot ltd*

I need a full website designed for for a 10,000m2 strorage facity which specialize in heavy commercial storage

it needs to be in english please

Target Market(s)

Comercial sector

Industry/Entity Type

Construction Company

Logo Text

KW

Coding

Coded - Design and coding required

Number of Pages Required

1 page

Font styles to use
Sans Serif

Colors
ec1f27
ffffff

Requirements
Must have
• Tel 0064 219486375
• email- mark@kwdepot.co.nz
Nice to have
• We specilize in large items with the facilty have 3 15tonne Gantry cranes and heavy mobile lifting equipment we can store items up to 20 tonne and we are fully covered and secure.
• square meter rates from 20m2 to 10,000 m2

```html
<!DOCTYPE html>
<html lang="en">
<head>
<meta charset="utf-8">
<title>KW Depot ltd – Heavy Commercial Storage</title>
<link rel="stylesheet" href="https://fonts.googleapis.com/css2?family=Montserrat:wght@900&family=Mulish:wght@400;600&display=swap">
<style>
:root{
  --red:#ec1f27;
  --white:#ffffff;
  --ink:#111111;
  --text:#2b2b2b;
  --grey-bg:#f0f0f0;
  --field-line:#a9a9a9;
  --footer:#151515;
  --footer-text:#e8e8e8;
  --hero-a:#33406a;
  --hero-b:#5a6178;
}
*{box-sizing:border-box;margin:0;padding:0}
html,body{width:1200px;height:2476px;overflow:hidden}
body{position:relative;background:var(--white);font-family:"Mulish",sans-serif;color:var(--text)}
.abs{position:absolute}
.heading{font-family:"Montserrat",sans-serif;font-weight:900;letter-spacing:3px;color:var(--ink);text-transform:uppercase}

/* header */
.brand{left:150px;top:36px;font-family:"Montserrat",sans-serif;font-weight:900;font-size:24px;color:var(--red);letter-spacing:1px;display:flex;align-items:center;gap:10px}
.brand-dot{width:14px;height:14px;border-radius:50%;background:var(--red)}
.contact-item{top:35px;display:flex;align-items:center;gap:15px;color:var(--red);font-size:12.5px;letter-spacing:1.2px}
.contact-icon{width:36px;height:36px;border:1.5px solid var(--red);border-radius:50%;display:flex;align-items:center;justify-content:center}

/* nav */
.nav{left:0;top:106px;width:1200px;height:54px;background:var(--red)}
.nav a{position:absolute;top:20px;transform:translateX(-50%);color:var(--white);text-decoration:none;font-weight:600;font-size:12.5px;letter-spacing:1.5px;white-space:nowrap}
.nav a.active{color:var(--ink);border-bottom:1.5px solid var(--ink);padding-bottom:2px}

/* hero */
.hero{left:0;top:160px;width:1200px;height:544px;background:linear-gradient(180deg,var(--hero-a) 0%,var(--hero-b) 60%,#6b6f7e 100%)}
.hero-title{left:0;width:1200px;top:148px;text-align:center;color:var(--white);font-size:34px;line-height:56px;letter-spacing:3.5px}
.hero-text{left:170px;width:860px;top:278px;text-align:center;color:var(--white);font-size:24px;line-height:29px;letter-spacing:2.6px}
.btn{background:var(--red);color:var(--white);font-size:14px;letter-spacing:1.3px;display:flex;align-items:center;justify-content:center}
.arrow{width:50px;height:50px;border:1.5px solid var(--red);border-radius:50%;display:flex;align-items:center;justify-content:center;top:248px}

/* services */
.section-title{left:0;width:1200px;text-align:center;font-size:29px;line-height:50px}
.card-photo{width:281px;height:197px;border-radius:5px;top:928px}
.card-title{width:281px;top:1163px;font-size:23px;line-height:40px;letter-spacing:2.5px}
.card-text{width:260px;top:1271px;font-size:13.5px;line-height:22.5px;letter-spacing:1.1px}

/* quote */
.quote{left:0;top:1437px;width:1200px;height:662px;background:var(--grey-bg)}
.field{border:1.5px solid var(--field-line);background:transparent;font-size:13.5px;letter-spacing:1.2px;color:#555;padding:19px 27px}

/* footer */
.footer{left:0;top:2099px;width:1200px;height:377px;background:var(--footer)}
.footer-brand{left:155px;top:2270px;font-family:"Montserrat",sans-serif;font-weight:900;font-size:30px;color:var(--red);letter-spacing:2px;display:flex;align-items:center;gap:12px}
.footer-head{top:2178px;font-size:18px;letter-spacing:2.5px;font-weight:600;color:var(--white)}
.footer-link{font-size:12.5px;letter-spacing:1.3px;color:var(--footer-text)}
.social{top:2344px;width:22px;height:22px;border-radius:50%;background:#3b5ad1}
.rule{left:150px;top:2428px;width:900px;height:1px;background:#3a3a3a}
</style>
</head>
<body>

<!-- header -->
<div class="abs brand"><span class="brand-dot"></span>KW Depot</div>

<div class="abs contact-item" style="left:586px">
  <span class="contact-icon">
    <svg width="16" height="16" viewBox="0 0 24 24" fill="none" stroke="#ec1f27" stroke-width="2"><path d="M5 3h4l2 5-2.5 1.5a11 11 0 0 0 6 6L16 13l5 2v4a2 2 0 0 1-2 2A16 16 0 0 1 3 5a2 2 0 0 1 2-2z"/></svg>
  </span>
  0064-219-486375
</div>
<div class="abs contact-item" style="left:825px">
  <span class="contact-icon">
    <svg width="14" height="11" viewBox="0 0 14 11"><rect width="14" height="11" rx="1" fill="#ec1f27"/><path d="M1 1l6 5 6-5" stroke="#fff" stroke-width="1.2" fill="none"/></svg>
  </span>
  mark@kwdepot.co.nz
</div>

<!-- navigation -->
<nav class="abs nav">
  <a class="active" style="left:271px">HOME</a>
  <a style="left:485px">WARE HOUSE STORAGE</a>
  <a style="left:714px">ABOUT US</a>
  <a style="left:904px">CONTACT US</a>
</nav>

<!-- hero -->
<section class="abs hero" role="img" aria-label="Interior of a large industrial warehouse with gantry cranes, tinted blue">
  <h1 class="abs heading hero-title" style="color:var(--white)">We specialize in large items within the<br>facility we have 15 tonne gantry cranes</h1>
  <p class="abs hero-text">Heavy mobile lifting equipment we can store items up to 20 tonne and we are fully covered and secure. Square meter rates from 20m2 to 10,000 m2</p>
  <div class="abs btn" style="left:531px;top:408px;width:139px;height:44px">Read More</div>
  <div class="abs arrow" style="left:68px">
    <svg width="20" height="12" viewBox="0 0 20 12" fill="none" stroke="#ec1f27" stroke-width="1.5"><path d="M19 6H2M7 1L2 6l5 5"/></svg>
  </div>
  <div class="abs arrow" style="left:1081px">
    <svg width="20" height="12" viewBox="0 0 20 12" fill="none" stroke="#ec1f27" stroke-width="1.5"><path d="M1 6h17M13 1l5 5-5 5"/></svg>
  </div>
</section>

<!-- services -->
<h2 class="abs heading section-title" style="top:795px">We pride ourselves in looking after all<br>your storage needs</h2>

<div class="abs card-photo" style="left:150px;background:linear-gradient(180deg,#3d4a72,#6b7488)" role="img" aria-label="Empty warehouse hall with overhead cranes"></div>
<div class="abs card-photo" style="left:460px;background:linear-gradient(180deg,#3a4468,#222a44)" role="img" aria-label="Staff member holding a tablet in the storage office"></div>
<div class="abs card-photo" style="left:769px;background:linear-gradient(180deg,#4a5370,#7a7a6e)" role="img" aria-label="Forklift carrying goods in the warehouse"></div>

<h3 class="abs heading card-title" style="left:150px">Need warehouse<br>space</h3>
<h3 class="abs heading card-title" style="left:460px">Your own<br>handling team</h3>
<h3 class="abs heading card-title" style="left:769px">Reliable<br>transportation</h3>

<p class="abs card-text" style="left:150px">We offer area space from 20m2 to 10,000 m2</p>
<p class="abs card-text" style="left:460px">Our handling team will look after all your storage needs 24hours a day</p>
<p class="abs card-text" style="left:769px">We will pack up and deliver your item if needed</p>

<!-- quote form -->
<section class="abs quote"></section>
<h2 class="abs heading section-title" style="top:1526px">Please contact us for a competitive quote</h2>
<div class="abs field" style="left:207px;top:1608px;width:374px;height:56px">First Name:</div>
<div class="abs field" style="left:619px;top:1608px;width:374px;height:56px">Last Name:</div>
<div class="abs field" style="left:207px;top:1690px;width:374px;height:56px">Email Address:</div>
<div class="abs field" style="left:619px;top:1690px;width:374px;height:56px">Phone Number:</div>
<div class="abs field" style="left:207px;top:1773px;width:786px;height:131px">Message:</div>
<div class="abs btn" style="left:519px;top:1953px;width:162px;height:45px">Send Message</div>

<!-- footer -->
<footer class="abs footer"></footer>
<div class="abs footer-brand"><span class="brand-dot" style="width:18px;height:18px"></span>KW Depot</div>

<div class="abs footer-head" style="left:439px">QUICK LINKS</div>
<div class="abs footer-link" style="left:439px;top:2244px">Home</div>
<div class="abs footer-link" style="left:439px;top:2276px">Ware House Storage</div>
<div class="abs footer-link" style="left:439px;top:2307px">About Us</div>
<div class="abs footer-link" style="left:439px;top:2338px">Contact Us</div>
<div class="abs footer-link" style="left:439px;top:2370px">More Info</div>

<div class="abs footer-head" style="left:690px">CONTACT</div>
<div class="abs footer-link" style="left:690px;top:2244px">EMAIL ADDRESS</div>
<div class="abs footer-link" style="left:690px;top:2276px">mark@kwdepot.co.nz</div>
<div class="abs footer-link" style="left:690px;top:2315px">PHONE</div>
<div class="abs footer-link" style="left:690px;top:2347px">0064-219-486375</div>

<div class="abs social" style="left:944px"></div>
<div class="abs social" style="left:972px;background:#2ea3e6"></div>
<div class="abs social" style="left:1000px;background:#c2349b"></div>
<div class="abs social" style="left:1027px;background:#1f6fb5"></div>

<div class="abs rule"></div>
<div class="abs footer-link" style="left:150px;top:2443px">Privacy &amp; Policy</div>
<div class="abs footer-link" style="left:885px;top:2443px">©2020. KW Depot LTD</div>

</body>
</html>
```